Velmora and Co Business Card Design

Looking for a business card design. Wanting Smart, Clean and Sharp looking to promote Velmora and Co, our Import Export Business - like Black, White and natural textures. I have uploaded our logo. I like a rounded font but open to other ideas
Being that we have a wide range of products on offer we are looking for a neutral yet eye catching card. We would also like to have Import - Export on the business card to be clear on want our business does.

Target Market(s)

Import export market

Industry/Entity Type

Importer

Contact Information for Business Card

Mr Tobias Kernwell
tobias.kernwell@velmoraandco.com.au
+61 (0) 417 630 284
www.velmoraandco.com.au

Font styles to use
Other font styles liked:
• Unsure of actual font name but something rounded and clean

Colors

Designer to choose colors to be used in the design.

Requirements
Must have
• Instagram icon
• Facebook icon

```html
<!DOCTYPE html>
<html lang="en">
<head>
<meta charset="utf-8">
<title>Velmora and Co Business Card</title>
<link href="https://fonts.googleapis.com/css2?family=Lato:wght@400;700&display=swap" rel="stylesheet">
<style>
  :root {
    --backdrop: #6f6f6f;
    --ink: #231f1f;
    --card-dark: #282323;
    --paper: #ffffff;
    --text-soft: #333333;
    --text-muted: #bdb8b8;
  }
  html, body {
    margin: 0;
    padding: 0;
    width: 1200px;
    height: 1200px;
    overflow: hidden;
    background: var(--backdrop);
    font-family: "Lato", sans-serif;
  }
  .canvas {
    position: relative;
    width: 1200px;
    height: 1200px;
  }
  .card {
    position: absolute;
    left: 192px;
    width: 813px;
    height: 464px;
    overflow: hidden;
  }
  .card--front {
    top: 78px;
    background: var(--card-dark);
  }
  .card--back {
    top: 660px;
    background: var(--paper);
  }
  .band {
    position: absolute;
    left: 0;
    top: 0;
    width: 100%;
    height: 246px;
    background: var(--card-dark);
  }
  .brand-block {
    position: absolute;
    left: 0;
    right: 0;
    display: flex;
    flex-direction: column;
    align-items: center;
    gap: 16px;
  }
  .card--front .brand-block { top: 160px; }
  .card--back .brand-block { top: 50px; }
  .brand {
    display: flex;
    align-items: center;
    gap: 18px;
    color: var(--paper);
    font-weight: 700;
  }
  .brand__square {
    width: 26px;
    height: 26px;
    background: var(--paper);
    flex: none;
  }
  .brand__name {
    font-size: 52px;
    line-height: 1.02;
    letter-spacing: 1px;
  }
  .tagline {
    margin: 0;
    color: var(--text-muted);
    font-size: 15px;
    font-weight: 400;
    letter-spacing: 5px;
    text-transform: uppercase;
  }
  .person {
    position: absolute;
    right: 421px;
    top: 343px;
    text-align: right;
    color: var(--ink);
  }
  .person__name {
    font-size: 27px;
    font-weight: 700;
    margin: 0;
    line-height: 1.1;
  }
  .person__role {
    font-size: 18px;
    margin: 6px 0 0;
    color: var(--text-soft);
  }
  .divider {
    position: absolute;
    left: 408px;
    top: 318px;
    width: 2px;
    height: 122px;
    background: var(--ink);
  }
  .contacts {
    position: absolute;
    left: 436px;
    top: 322px;
    margin: 0;
    padding: 0;
    list-style: none;
    color: var(--ink);
    font-size: 15.5px;
  }
  .contacts li {
    display: flex;
    align-items: center;
    gap: 9px;
    height: 28px;
  }
  .contacts svg {
    width: 14px;
    height: 14px;
    flex: none;
  }
  .social-dots {
    display: flex;
    gap: 4px;
  }
</style>
</head>
<body>
<main class="canvas">
  <section class="card card--front" role="img" aria-label="Dark card face with a faint chevron texture">
    <div class="brand-block">
      <div class="brand">
        <span class="brand__square"></span>
        <span class="brand__name">Velmora<br>and Co</span>
      </div>
      <p class="tagline">Import - Export</p>
    </div>
  </section>

  <section class="card card--back">
    <div class="band" role="img" aria-label="Dark band with a faint chevron texture"></div>
    <div class="brand-block">
      <div class="brand">
        <span class="brand__square"></span>
        <span class="brand__name">Velmora<br>and Co</span>
      </div>
      <p class="tagline">Import - Export</p>
    </div>

    <div class="person">
      <p class="person__name">Mr Tobias Kernwell</p>
      <p class="person__role">CEO &amp; Manager</p>
    </div>
    <div class="divider"></div>

    <ul class="contacts">
      <li>
        <svg viewBox="0 0 16 16" aria-hidden="true"><path d="M3.5 1.5l2.5 0 1 3.5-1.7 1.2a9 9 0 0 0 4.5 4.5l1.2-1.7 3.5 1v2.5c0 .8-.7 1.5-1.5 1.5A12.5 12.5 0 0 1 2 3c0-.8.7-1.5 1.5-1.5z" fill="#231f1f"/></svg>
        <span>+61 (0) 417 630 284</span>
      </li>
      <li>
        <svg viewBox="0 0 16 16" aria-hidden="true"><rect x="3.5" y="1" width="9" height="14" rx="4.5" fill="#231f1f"/><line x1="8" y1="2.5" x2="8" y2="6" stroke="#fff" stroke-width="1.2"/></svg>
        <span>tobias.kernwell@velmoraandco.com.au</span>
      </li>
      <li>
        <svg viewBox="0 0 16 16" aria-hidden="true" fill="none" stroke="#231f1f" stroke-width="1.3"><circle cx="8" cy="8" r="6.5"/><ellipse cx="8" cy="8" rx="2.8" ry="6.5"/><line x1="1.5" y1="8" x2="14.5" y2="8"/></svg>
        <span>www.velmoraandco.com.au</span>
      </li>
      <li>
        <span class="social-dots" role="img" aria-label="Social media accounts">
          <svg viewBox="0 0 16 16" aria-hidden="true"><circle cx="8" cy="8" r="7" fill="#231f1f"/></svg>
          <svg viewBox="0 0 16 16" aria-hidden="true"><circle cx="8" cy="8" r="7" fill="#231f1f"/></svg>
        </span>
        <span>@velmoraandco</span>
      </li>
    </ul>
  </section>
</main>
</body>
</html>
```